V STUDIO Interior & Exterior Designer Business needs a Business Card

V STUDIO - I need a Business Card Design for a Interior Design Business, I work Nationally Around Australia on Projects specialising In AGED CARE and would like to rebrand and change the Look.
I work mainly with Large Corporate Companys, Select everything From External Finishes to All Internal Finishes, Furniture and then Decorate to a 5 star finish.

Industry/Entity Type

Business

Contact Information for Business Card

V STUDIO
Marlena Hobart
PH: (+61) 0400 872 634
E: lenny@vstudiohub.example

Font styles to use
Sans Serif

Requirements
Must have
• My Priject Must Have a Contemporary Design, Bold, Eye Catching, that makes a statement but MUST BE ELEGANT - 2 or 3 Colours - Strong Power Colours.
• 2 sided
• i like the works - IMAGEN, DESIGN, CREATE
Nice to have
• I would like the words ' imagine design create ' incorporated into the design
• I like Some Red on the card

```html
<!DOCTYPE html>
<html lang="en">
<head>
<meta charset="utf-8">
<title>V STUDIO – Business Card Colour Options</title>
<link rel="stylesheet" href="https://fonts.googleapis.com/css2?family=Josefin+Sans:wght@300;400&display=swap">
<style>
  :root {
    --sheet-light: #ffffff;
    --sheet-grey: #b5b6b8;
    --card-white: #ffffff;
    --ink-dark: #1a1a1a;
    --ink-light: #ffffff;
    --amber: #e09e17;
    --ochre: #c8a30a;
    --saffron: #efb21a;
    --citron: #e0df35;
  }
  * { box-sizing: border-box; margin: 0; padding: 0; }
  html, body { width: 1200px; height: 995px; overflow: hidden; }
  body {
    font-family: "Josefin Sans", sans-serif;
    background: linear-gradient(to right, var(--sheet-light) 700px, var(--sheet-grey) 800px);
  }
  .sheet {
    position: absolute; left: 22px; top: 43px;
    display: grid;
    grid-template-columns: 378px 377px 377px;
    grid-template-rows: repeat(4, 210px);
    column-gap: 9px; row-gap: 18px;
  }
  .option--amber { --tone: var(--amber); }
  .option--ochre { --tone: var(--ochre); }
  .option--saffron { --tone: var(--saffron); }
  .option--citron { --tone: var(--citron); }

  .card { position: relative; border-radius: 14px; overflow: hidden; }
  .card--front { background: var(--tone); }
  .card--back { background: var(--card-white); }

  .card--front-light { color: var(--ink-light); }
  .card--front-dark { color: var(--ink-dark); }

  .front-square { position: absolute; left: 66px; top: 77px; width: 55px; height: 55px; background: currentColor; }
  .front-name {
    position: absolute; left: 136px; top: 82px;
    font-size: 30px; font-weight: 400; letter-spacing: 2px; line-height: 30px; white-space: nowrap;
  }
  .front-motto {
    position: absolute; left: 138px; top: 121px;
    font-size: 9px; font-weight: 300; letter-spacing: 2.4px; line-height: 10px; white-space: nowrap;
  }

  .back-square { position: absolute; left: 33px; top: 41px; width: 89px; height: 89px; background: var(--tone); }
  .back-name {
    position: absolute; left: 33px; top: 150px;
    font-size: 16px; font-weight: 400; letter-spacing: 1px; line-height: 16px; color: var(--tone); white-space: nowrap;
  }

  .holder-name { position: absolute; left: 153px; top: 48px; font-size: 16px; font-weight: 300; letter-spacing: 3px; color: var(--tone); white-space: nowrap; }
  .contact { position: absolute; left: 153px; font-size: 10.5px; letter-spacing: 1.4px; color: var(--ink-dark); white-space: nowrap; }
  .contact--phone { top: 138px; }
  .contact--email { top: 160px; }
</style>
</head>
<body>
<main class="sheet">
  <section class="card card--front card--front-light option--amber">
    <div class="front-square"></div><p class="front-name">V STUDIO</p><p class="front-motto">PLAN • FURNISH • FINISH</p>
  </section>
  <section class="card card--front card--front-dark option--amber">
    <div class="front-square"></div><p class="front-name">V STUDIO</p><p class="front-motto">PLAN • FURNISH • FINISH</p>
  </section>
  <section class="card card--back option--amber">
    <div class="back-square"></div><p class="back-name">V STUDIO</p>
    <p class="holder-name">Marlena Hobart</p>
    <p class="contact contact--phone">(+61) 0400 872 634</p>
    <p class="contact contact--email">lenny@vstudiohub.example</p>
  </section>

  <section class="card card--front card--front-light option--ochre">
    <div class="front-square"></div><p class="front-name">V STUDIO</p><p class="front-motto">PLAN • FURNISH • FINISH</p>
  </section>
  <section class="card card--front card--front-dark option--ochre">
    <div class="front-square"></div><p class="front-name">V STUDIO</p><p class="front-motto">PLAN • FURNISH • FINISH</p>
  </section>
  <section class="card card--back option--ochre">
    <div class="back-square"></div><p class="back-name">V STUDIO</p>
    <p class="holder-name">Marlena Hobart</p>
    <p class="contact contact--phone">(+61) 0400 872 634</p>
    <p class="contact contact--email">lenny@vstudiohub.example</p>
  </section>

  <section class="card card--front card--front-light option--saffron">
    <div class="front-square"></div><p class="front-name">V STUDIO</p><p class="front-motto">PLAN • FURNISH • FINISH</p>
  </section>
  <section class="card card--front card--front-dark option--saffron">
    <div class="front-square"></div><p class="front-name">V STUDIO</p><p class="front-motto">PLAN • FURNISH • FINISH</p>
  </section>
  <section class="card card--back option--saffron">
    <div class="back-square"></div><p class="back-name">V STUDIO</p>
    <p class="holder-name">Marlena Hobart</p>
    <p class="contact contact--phone">(+61) 0400 872 634</p>
    <p class="contact contact--email">lenny@vstudiohub.example</p>
  </section>

  <section class="card card--front card--front-light option--citron">
    <div class="front-square"></div><p class="front-name">V STUDIO</p><p class="front-motto">PLAN • FURNISH • FINISH</p>
  </section>
  <section class="card card--front card--front-dark option--citron">
    <div class="front-square"></div><p class="front-name">V STUDIO</p><p class="front-motto">PLAN • FURNISH • FINISH</p>
  </section>
  <section class="card card--back option--citron">
    <div class="back-square"></div><p class="back-name">V STUDIO</p>
    <p class="holder-name">Marlena Hobart</p>
    <p class="contact contact--phone">(+61) 0400 872 634</p>
    <p class="contact contact--email">lenny@vstudiohub.example</p>
  </section>
</main>
</body>
</html>
```